Property Development Business Cards

I need a business card design for Blue Harbour Developments Pty Ltd. We are a property development company in Australia and our name defines the five values that we adhere to, being Profitable, Partnerships, Quality Developments, Eco Friendly and Enduring Design.

I have attached the current logo that I use, it is just five yellow circles connected to a single cricle in the middle.

Target Market(s)

Our Target audience is real estate agents, owners of properties, builders and other trades

Industry/Entity Type

Business

Requirements
Must have
• Want to have two sides to the card, one with details and one to just highlight the company

```html
<!DOCTYPE html>
<html lang="en">
<head>
<meta charset="utf-8">
<title>Blue Harbour Developments – Business Cards</title>
<link rel="stylesheet" href="https://fonts.googleapis.com/css2?family=Arimo&family=Tinos:wght@700&display=swap">
<style>
  :root {
    --page: #efefef;
    --card: #ffffff;
    --ink: #1f1f1f;
    --gold: #f2b600;
    --red: #d9141c;
    --orange: #f2861e;
    --yellow: #fbb714;
    --green: #8cc63f;
    --blue: #1aa6e0;
    --magenta: #e6197f;
    --purple: #6a2f8f;
    --plum: #9b1f5c;
  }
  * { margin: 0; padding: 0; box-sizing: border-box; }
  html, body { width: 1008px; height: 1200px; overflow: hidden; }
  body { background: var(--page); position: relative; }

  .card {
    position: absolute;
    left: 107px;
    width: 780px;
    height: 458px;
    background: var(--card);
    border-radius: 28px;
    overflow: hidden;
  }
  .card--front { top: 105px; }
  .card--back { top: 631px; }

  .pattern {
    position: absolute;
    border-radius: 26px;
  }
  .card--front .pattern {
    inset: 0;
    border-radius: 0;
    background:
      linear-gradient(120deg, var(--red) 0%, var(--orange) 22%, var(--yellow) 38%, var(--green) 52%, var(--blue) 66%, var(--magenta) 80%, var(--purple) 100%);
  }
  .card--back .pattern {
    left: 480px; top: 28px;
    width: 278px; height: 288px;
    background:
      linear-gradient(135deg, var(--red) 0%, var(--plum) 25%, var(--yellow) 45%, var(--blue) 65%, var(--magenta) 80%, var(--green) 100%);
  }

  .brand-mark {
    position: absolute;
    left: 172px; top: 40px;
    width: 60px; height: 60px;
    border-radius: 50%;
    background: var(--gold);
  }
  .company {
    position: absolute;
    left: 72px; top: 168px;
    font-family: "Tinos", "Times New Roman", serif;
    font-weight: 700;
    font-size: 21px;
    color: var(--ink);
    white-space: nowrap;
  }
  .details {
    position: absolute;
    left: 76px; top: 220px;
    font-family: "Arimo", Arial, sans-serif;
    font-size: 22px;
    font-variant: small-caps;
    line-height: 28px;
    color: var(--ink);
    list-style: none;
    white-space: nowrap;
  }
  .email {
    position: absolute;
    right: 26px; top: 404px;
    font-family: "Arimo", Arial, sans-serif;
    font-size: 22px;
    font-variant: small-caps;
    color: var(--ink);
    white-space: nowrap;
  }
</style>
</head>
<body>
  <section class="card card--front" aria-label="Card front">
    <div class="pattern" role="img" aria-label="Overlapping coloured rounded squares in red, orange, yellow, green, blue, magenta and purple"></div>
  </section>

  <section class="card card--back" aria-label="Card back">
    <span class="brand-mark" aria-hidden="true"></span>
    <h1 class="company">Blue Harbour Developments Pty Ltd.</h1>
    <ul class="details">
      <li>Daniel Hartwell,</li>
      <li>PO Box NO.218,</li>
      <li>Kenwick, ACT 2913,</li>
      <li>Mobile : 0400 555 182.</li>
    </ul>
    <div class="pattern" role="img" aria-label="Cluster of overlapping coloured rounded squares"></div>
    <p class="email">Daniel@BlueHarbourDevelopments.com.au</p>
  </section>
</body>
</html>
```